Redesign cement bags for leading cement producer in south east asia

We are from Larkfield cement and would like to redesign our bag to relaunch the product line. Our bags are made of high quality PP woven sack. We are one of the leading cement producers and we want our bags to have a Larkfield classy look on each visible side when it is loading in a truck or stacking on a pallet.

Thank you for interesting in this project. Good luck.

Project Deadline Extended Reason: Hi all, I have received requests to extend the deadline. Some of the work requires revising and some of them are still on process. To be fair, I also raise my budget to compensate the time. Thanks all for your participation. Added Sunday, July 10, 2016

Target Market(s)

Construction

Industry/Entity Type

Cement

Requirements
Must have
• You will have to design two bags for two cement grades. 52.5 is of higher grade and 42.5 is of lower grade. Both are similar in design but a distinctive colours to differentiate the two at once. Please look at Reference picture 2 for ideas.
Nice to have
• You do not have to change the original logo but the Larkfield cement word font changes are required. There are no restrictions to colours and font but please refrain from using feminine colours. Instructions on rear side of the bags are now included in the scope. Please create new layout and design new user friendly symbols.
Should not have
• Since cement is a dusty product, you need avoid some colours like black as background. The dust need to be less obvious to attract attention. Our previous base colour are shown in below.
• We want a fresh look on our bag, please do not just copy our old design and make small changes. I have attached our competitors' design, please refrain from using their design as well.
• It is recommend to do some research on cement bag sector.

```html
<!DOCTYPE html>
<html lang="en">
<head>
<meta charset="utf-8">
<title>Larkfield Cement – 42.5 Bag</title>
<link rel="stylesheet" href="https://fonts.googleapis.com/css2?family=Bebas+Neue&family=Raleway:wght@200&display=swap">
<style>
  :root {
    --cyan: #00aeef;
    --navy: #0f3a73;
    --deep-navy: #0a1a45;
    --red: #ed1c24;
    --dark-red: #8e0408;
    --band-grey: #939598;
    --text-grey: #6d6e71;
    --paper: #ffffff;
  }
  * { margin: 0; padding: 0; box-sizing: border-box; }
  html, body { width: 800px; height: 1200px; overflow: hidden; background: var(--paper); }
  .bag {
    position: relative;
    width: 800px;
    height: 1200px;
    background: var(--paper);
    overflow: hidden;
  }
  .brand-mark {
    position: absolute;
    left: 340px; top: 40px;
    width: 120px; height: 120px;
    border-radius: 50%;
    background: var(--navy);
  }
  .brand-name {
    position: absolute;
    left: 0; right: 0; top: 192px;
    text-align: center;
    font-family: "Bebas Neue", sans-serif;
    font-size: 188px;
    line-height: 1;
    color: var(--cyan);
  }
  .product-band {
    position: absolute;
    left: 130px; top: 349px;
    width: 540px; height: 72px;
    background: var(--band-grey);
    color: var(--paper);
    font-family: "Raleway", sans-serif;
    font-weight: 200;
    font-size: 54px;
    line-height: 72px;
    letter-spacing: 42px;
    text-indent: 42px;
    text-align: center;
  }
  .spec {
    position: absolute;
    left: 0; right: 0; top: 442px;
    text-align: center;
    font-family: "Bebas Neue", sans-serif;
    font-size: 28px;
    line-height: 32px;
    color: var(--text-grey);
  }
  .artwork {
    position: absolute;
    left: 0; top: 0;
  }
  .grade-bar {
    position: absolute;
    left: 0; top: 1092px;
    width: 600px; height: 108px;
    background: var(--cyan);
    color: var(--paper);
    font-family: "Bebas Neue", sans-serif;
  }
  .grade-bar .grade {
    position: absolute;
    left: 14px; top: 14px;
    font-size: 92px;
    line-height: 1;
  }
  .grade-bar .tagline {
    position: absolute;
    left: 143px; top: 22px;
    font-size: 32px;
    line-height: 33px;
  }
  .weight {
    position: absolute;
    left: 612px; top: 1000px;
    font-family: "Bebas Neue", sans-serif;
    font-size: 150px;
    line-height: 1;
    color: var(--text-grey);
  }
</style>
</head>
<body>
  <main class="bag">
    <div class="brand-mark"></div>
    <h1 class="brand-name">LARKFIELD</h1>
    <div class="product-band">CEMENT</div>
    <p class="spec">PORTLAND CEMENT<br>EN 197-1 (2000) , STRENGTH CLASS 42.5</p>

    <svg class="artwork" width="800" height="1200" viewBox="0 0 800 1200" role="img"
         aria-label="Geometric composition of overlapping blue, navy and red triangles with small stars">
      <defs>
        <linearGradient id="geo-tones" x1="0" y1="1" x2="1" y2="0">
          <stop offset="0" stop-color="#ed1c24"/>
          <stop offset="0.35" stop-color="#8e0408"/>
          <stop offset="0.6" stop-color="#0f3a73"/>
          <stop offset="1" stop-color="#00aeef"/>
        </linearGradient>
      </defs>
      <polygon points="0,1092 600,1092 600,990 800,900 800,610 600,585 330,585 0,880"
               fill="url(#geo-tones)"/>
    </svg>

    <div class="grade-bar">
      <span class="grade">42.5</span>
      <span class="tagline">CEMENT EXPORT QUALITY<br>PRODUCT OF MYANMAR</span>
    </div>
    <div class="weight">50</div>
  </main>
</body>
</html>
```